Fast growing Tech company needs redesign of Veltrana's end user website!

We need to have our login screen, the dashboard, and the one page of the Veltrana site to be redesigned for the end-users. Veltrana is a document hosting service for title companies and real estate law firms. This allows the buyers and sellers to view their closing documents after closing along with many other features that help them out during the closing of their property. More information about what we do can be found on our test site https://qpx.524.sampledraft-host.com/. PLEASE NOTE: THE ABOVE SITE IS NOT THE ONE WE NEED REDONE. The above site is our corporate site that explains our service offering and we thought it would be helpful in providing you a better understanding of our service.
The site that we want to have redesigned is for the end user. THE SITE THAT NEEDS TO BE REDONE ARE THE SCREENSHOTS ATTACHED. We will need the login screen, dashboard, and the one page redesigned.
.
We will just need this in HTML and we will then do the rest for the placeholders for logos, data, mapping etc.
Overall, we want a new, fresh, and modern look for the website and we want the login screen, dashboard and one page website to be consistent in design. Again, these are the three screenshots that are attached.
For the winner, we will most likely need to hire you again for more sites because we have other versions.
Thank you and if any questions, please let us know.
Target Market(s)
This site is for buyer and sellers during the closing process of real estate transaction.

```html
<!DOCTYPE html>
<html lang="en">
<head>
<meta charset="utf-8">
<title>Veltrana – Closing Dashboard</title>
<link href="https://fonts.googleapis.com/css2?family=Lato:wght@400;700&display=swap" rel="stylesheet">
<style>
:root{
  --blue:#2ea3d8;
  --blue-dark:#2590c4;
  --ink:#2e2e2e;
  --muted:#444;
  --cream:#fbf0e3;
  --line:#3aa3d9;
  --grey-pill:#c9c9c9;
  --hero-top:#1c2a3d;
  --hero-bottom:#4a3a2c;
}
*{box-sizing:border-box;margin:0;padding:0}
html,body{width:1200px;height:3905px;overflow:hidden}
body{font-family:'Lato',sans-serif;color:var(--ink);background:#fff;position:relative}
.abs{position:absolute}

/* hero */
.hero{left:0;top:0;width:1200px;height:645px}
.nav-logo{left:136px;top:22px;font-size:26px;color:#fff;font-weight:400;letter-spacing:.5px}
.nav-link{top:30px;font-size:14px;color:#fff}
.btn-signout{left:1015px;top:24px;width:99px;height:28px;background:var(--blue);color:#fff;font-size:13px;display:flex;align-items:center;justify-content:center;border-radius:2px}
.hero-title{left:0;top:108px;width:1200px;text-align:center;color:#fff;font-size:42px;line-height:49px;font-weight:400}

/* welcome */
.welcome-title{left:136px;top:693px;font-size:30px;font-weight:400}
.welcome-text{left:136px;top:763px;width:610px;font-size:14px;line-height:18px;color:var(--muted)}
.avatar{left:931px;top:669px;width:128px;height:128px;border-radius:50%;background:radial-gradient(circle at 50% 40%,#6b7b8f,#1f2836)}
.btn-outline{border:2px solid var(--blue-dark);color:var(--ink);background:#fff;display:flex;align-items:center;justify-content:center;font-size:13px;border-radius:3px}

/* section headings */
.section-head{left:0;width:1200px;text-align:center;font-size:30px;font-weight:700;letter-spacing:.5px;color:#2b2b2b}
.rule{height:2px;background:var(--line)}
.dot{width:12px;height:12px;border-radius:50%;background:var(--line)}

/* info cards */
.card{background:var(--cream);box-shadow:0 2px 6px rgba(0,0,0,.18);border-radius:3px}
.card-title{color:var(--blue);font-size:20px;font-weight:400;position:absolute;left:43px;top:18px;letter-spacing:.3px}
.card-body{position:absolute;left:43px;font-size:14px;line-height:22px;color:var(--ink)}
.card-body b{font-weight:700}
.card-icon{position:absolute;left:10px;top:14px}
.map{left:624px;top:1076px;width:441px;height:296px;border-radius:4px;background:linear-gradient(135deg,#4f5a3c,#7b7b6c 50%,#5b6a4a)}
.btn-fill{background:var(--blue);color:#fff;display:flex;align-items:center;justify-content:center;font-size:13px;border-radius:2px}

/* milestones */
.ms-icon{width:50px;height:50px;border-radius:50%;border:2px solid #ddd;display:flex;align-items:center;justify-content:center}
.ms-icon.done{border-color:var(--blue)}
.ms-title{font-size:20px;color:var(--ink)}
.ms-title.done{color:var(--blue)}
.ms-sub{font-size:14px;color:var(--muted)}
.pill{width:124px;height:23px;border-radius:3px;color:#fff;font-size:9px;letter-spacing:.5px;display:flex;align-items:center;justify-content:center}
.pill.done{background:var(--blue)}
.pill.pending{background:var(--grey-pill)}

/* panels */
.panel{background:var(--cream);box-shadow:0 2px 6px rgba(0,0,0,.18)}
.panel-title{position:absolute;left:33px;top:20px;font-size:30px;font-weight:700;color:#2b2b2b}
.panel-rule{position:absolute;left:0;right:0;top:64px;height:2px;background:var(--line)}
.doc-title{font-size:20px;color:var(--blue)}
.doc-sub{font-size:11px;color:var(--muted)}
.wire-label{font-size:14px;font-weight:700;color:var(--ink)}
.wire-value{font-size:11px;color:var(--muted)}

/* professionals */
.photo{width:207px;height:208px;border-radius:3px}
.pro-name{font-size:20px;color:var(--blue)}
.pro-co{font-size:14px;color:var(--muted)}
.icon-btn{width:41px;height:40px;background:var(--blue);border-radius:3px;display:flex;align-items:center;justify-content:center}

/* faq */
.faq{background:var(--blue);color:#fff;border-radius:3px}
.faq-q{position:absolute;left:20px;font-size:20px}
.faq-a{position:absolute;left:20px;top:55px;width:740px;font-size:14px;line-height:18px}
.faq-chev{position:absolute;right:32px}

/* footer */
.footer{left:0;top:3620px;width:1200px;height:285px}
.footer-text{color:#fff;font-size:14px;display:flex;align-items:center;gap:10px}
.footer-logo{left:0;top:3676px;width:1200px;text-align:center;color:#fff;font-size:46px;font-weight:400}
.footer-copy{left:0;top:3864px;width:1200px;text-align:center;color:#fff;font-size:11px}
</style>
</head>
<body>

<!-- hero -->
<svg class="abs hero" viewBox="0 0 1200 645" role="img" aria-label="Photo of a modern wooden house entrance at dusk">
  <defs>
    <linearGradient id="heroGrad" x1="0" y1="0" x2="0" y2="1">
      <stop offset="0" stop-color="#243449"/>
      <stop offset=".55" stop-color="#2e3744"/>
      <stop offset="1" stop-color="#3f3428"/>
    </linearGradient>
  </defs>
  <polygon points="0,0 1200,0 1200,560 600,645 0,560" fill="url(#heroGrad)"/>
</svg>
<div class="abs nav-logo">Veltrana</div>
<div class="abs nav-link" style="left:820px">Dashboard</div>
<div class="abs nav-link" style="left:918px">My Profile</div>
<div class="abs btn-signout">SIGN OUT</div>
<div class="abs hero-title">Keeping you informed during<br>your closing</div>

<!-- welcome -->
<div class="abs welcome-title">Welcome Clark Buyer!</div>
<p class="abs welcome-text">On behalf of all of us at The Real Estate Law Firm, we would like to thank you for choosing us for the closing of your property. Because we want you to be informed at every step of the process, we use the Innovative Digital Cosing Package to keep all parties involved in the transaction on the same page for a smooth and successful closing</p>
<div class="abs avatar" role="img" aria-label="Profile photo of the buyer"></div>
<div class="abs btn-outline" style="left:912px;top:811px;width:167px;height:48px">VIEW PROFILE</div>

<!-- transactional information -->
<div class="abs rule" style="left:136px;top:974px;width:190px"></div>
<div class="abs dot" style="left:320px;top:969px"></div>
<div class="abs dot" style="left:865px;top:969px"></div>
<div class="abs rule" style="left:871px;top:974px;width:194px"></div>
<div class="abs section-head" style="top:955px">TRANSACTIONAL INFORMATION</div>

<div class="abs card" style="left:135px;top:1076px;width:421px;height:154px">
  <svg class="card-icon" width="26" height="26" viewBox="0 0 26 26"><rect x="3" y="8" width="14" height="12" rx="2" fill="none" stroke="#2ea3d8" stroke-width="2"/><circle cx="19" cy="7" r="5" fill="none" stroke="#2ea3d8" stroke-width="2"/></svg>
  <div class="card-title">YOUR TRANSACTION INFORMATION</div>
  <div class="card-body" style="top:50px"><b>File Number:</b>&nbsp; 2018-015987<br><b>Buyer:</b>&nbsp; Clark Buyer<br><b>Seller:</b>&nbsp; Chloe Seller<br><b>Agent:</b>&nbsp; Bob Buyer Agent</div>
</div>
<div class="abs card" style="left:135px;top:1242px;width:421px;height:103px">
  <svg class="card-icon" width="26" height="28" viewBox="0 0 26 28"><path d="M13 2a7 7 0 0 1 7 7c0 5-7 12-7 12S6 14 6 9a7 7 0 0 1 7-7z" fill="#2ea3d8"/><circle cx="13" cy="9" r="2.5" fill="#fbf0e3"/><ellipse cx="13" cy="24" rx="8" ry="2" fill="none" stroke="#2ea3d8" stroke-width="1.5"/></svg>
  <div class="card-title">PROPERTY ADDRESS</div>
  <div class="card-body" style="top:52px;line-height:18px">2400 Maple Street<br>Miami, FL 33155</div>
</div>
<div class="abs card" style="left:135px;top:1357px;width:421px;height:103px">
  <svg class="card-icon" width="26" height="28" viewBox="0 0 26 28"><path d="M5 3h11l5 5v17H5z" fill="#2ea3d8"/><circle cx="19" cy="20" r="5" fill="#fbf0e3" stroke="#2ea3d8" stroke-width="2"/></svg>
  <div class="card-title">PURCHASE DETAILS</div>
  <div class="card-body" style="top:50px"><b>Purchase Price:</b>&nbsp;&nbsp;&nbsp; $580,000<br><b>Settlement Date:</b>&nbsp;&nbsp; Tuesday, December 25, 2018</div>
</div>
<div class="abs map" role="img" aria-label="Aerial map of the property location with a pin"></div>
<svg class="abs" style="left:872px;top:1150px" width="24" height="32" viewBox="0 0 24 32"><path d="M12 1a10 10 0 0 1 10 10c0 8-10 20-10 20S2 19 2 11A10 10 0 0 1 12 1z" fill="#2ea3d8"/><circle cx="12" cy="11" r="4" fill="#fff"/></svg>
<div class="abs btn-fill" style="left:761px;top:1412px;width:166px;height:50px">VIEW FULL MAP</div>

<!-- closing milestones -->
<div class="abs rule" style="left:136px;top:1553px;width:267px"></div>
<div class="abs dot" style="left:397px;top:1548px"></div>
<div class="abs dot" style="left:790px;top:1548px"></div>
<div class="abs rule" style="left:796px;top:1553px;width:269px"></div>
<div class="abs section-head" style="top:1534px">CLOSING MILESTONES</div>

<!-- row 1 -->
<div class="abs ms-icon done" style="left:151px;top:1629px"><svg width="24" height="18" viewBox="0 0 24 18"><path d="M2 9l7 7L22 2" fill="none" stroke="#2ea3d8" stroke-width="2.5"/></svg></div>
<div class="abs ms-title done" style="left:217px;top:1630px">Transaction Started</div>
<div class="abs ms-sub" style="left:217px;top:1662px">Clark Buyer connect with Chloe Seller</div>
<div class="abs pill done" style="left:720px;top:1643px">COMPLETED</div>
<div class="abs btn-outline" style="left:912px;top:1630px;width:135px;height:49px">VIEW DETAILS</div>
<!-- row 2 -->
<div class="abs ms-icon done" style="left:151px;top:1710px"><svg width="24" height="18" viewBox="0 0 24 18"><path d="M2 9l7 7L22 2" fill="none" stroke="#2ea3d8" stroke-width="2.5"/></svg></div>
<div class="abs ms-title done" style="left:217px;top:1711px">Earnest Money Recieved</div>
<div class="abs ms-sub" style="left:217px;top:1743px">Chloe Seller pays Clark Buyer the earnest money</div>
<div class="abs pill done" style="left:720px;top:1724px">COMPLETED</div>
<div class="abs btn-outline" style="left:912px;top:1711px;width:135px;height:49px">VIEW DETAILS</div>
<!-- pending rows -->
<div class="abs ms-icon" style="left:151px;top:1790px"><svg width="16" height="16" viewBox="0 0 16 16"><circle cx="8" cy="8" r="7" fill="#ccc"/><rect x="7" y="7" width="2" height="5" fill="#fff"/><rect x="7" y="4" width="2" height="2" fill="#fff"/></svg></div>
<div class="abs ms-title" style="left:217px;top:1791px">Delivery Title Report</div>
<div class="abs ms-sub" style="left:217px;top:1823px">Not completed yet</div>
<div class="abs pill pending" style="left:720px;top:1804px">PENDING</div>

<div class="abs ms-icon" style="left:151px;top:1871px"><svg width="16" height="16" viewBox="0 0 16 16"><circle cx="8" cy="8" r="7" fill="#ccc"/><rect x="7" y="7" width="2" height="5" fill="#fff"/><rect x="7" y="4" width="2" height="2" fill="#fff"/></svg></div>
<div class="abs ms-title" style="left:217px;top:1872px">Title Cleared</div>
<div class="abs ms-sub" style="left:217px;top:1904px">Not completed yet</div>
<div class="abs pill pending" style="left:720px;top:1885px">PENDING</div>

<div class="abs ms-icon" style="left:151px;top:1951px"><svg width="16" height="16" viewBox="0 0 16 16"><circle cx="8" cy="8" r="7" fill="#ccc"/><rect x="7" y="7" width="2" height="5" fill="#fff"/><rect x="7" y="4" width="2" height="2" fill="#fff"/></svg></div>
<div class="abs ms-title" style="left:217px;top:1952px">Signing Scheduled</div>
<div class="abs ms-sub" style="left:217px;top:1984px">Not completed yet</div>
<div class="abs pill pending" style="left:720px;top:1965px">PENDING</div>

<div class="abs ms-icon" style="left:151px;top:2032px"><svg width="16" height="16" viewBox="0 0 16 16"><circle cx="8" cy="8" r="7" fill="#ccc"/><rect x="7" y="7" width="2" height="5" fill="#fff"/><rect x="7" y="4" width="2" height="2" fill="#fff"/></svg></div>
<div class="abs ms-title" style="left:217px;top:2033px">Transaction Closed</div>
<div class="abs ms-sub" style="left:217px;top:2065px">Not completed yet</div>
<div class="abs pill pending" style="left:720px;top:2046px">PENDING</div>

<!-- documents panel -->
<div class="abs panel" style="left:135px;top:2171px;width:459px;height:470px">
  <div class="panel-title">VIEW DOCUMENTS</div>
  <div class="panel-rule"></div>
</div>
<!-- doc rows -->
<div class="abs" style="left:170px;top:2275px"><svg width="34" height="48" viewBox="0 0 34 48"><path d="M0 0h24l10 10v38H0z" fill="#2ea3d8"/><path d="M7 18h20M7 25h20M7 32h20M7 39h20" stroke="#fff" stroke-width="2"/></svg></div>
<div class="abs doc-title" style="left:232px;top:2275px">Closing Paper Work</div>
<div class="abs doc-sub" style="left:232px;top:2307px">Uploaded by Bob Buyer Agent</div>
<div class="abs btn-outline" style="left:462px;top:2276px;width:99px;height:50px">VIEW</div>

<div class="abs" style="left:170px;top:2345px"><svg width="34" height="48" viewBox="0 0 34 48"><path d="M0 0h24l10 10v38H0z" fill="#2ea3d8"/><path d="M7 18h20M7 25h20M7 32h20M7 39h20" stroke="#fff" stroke-width="2"/></svg></div>
<div class="abs doc-title" style="left:232px;top:2345px">Purchase Agreement</div>
<div class="abs doc-sub" style="left:232px;top:2377px">Uploaded by Chloe Buyer</div>
<div class="abs btn-outline" style="left:462px;top:2346px;width:99px;height:50px">VIEW</div>

<div class="abs" style="left:170px;top:2414px"><svg width="34" height="48" viewBox="0 0 34 48"><path d="M0 0h24l10 10v38H0z" fill="#2ea3d8"/><path d="M7 18h20M7 25h20M7 32h20M7 39h20" stroke="#fff" stroke-width="2"/></svg></div>
<div class="abs doc-title" style="left:232px;top:2414px">Purchase Agreement</div>
<div class="abs doc-sub" style="left:232px;top:2446px">Uploaded by Chloe Buyer</div>
<div class="abs btn-outline" style="left:462px;top:2415px;width:99px;height:50px">VIEW</div>

<div class="abs" style="left:170px;top:2484px"><svg width="34" height="48" viewBox="0 0 34 48"><path d="M0 0h24l10 10v38H0z" fill="#2ea3d8"/><path d="M7 18h20M7 25h20M7 32h20M7 39h20" stroke="#fff" stroke-width="2"/></svg></div>
<div class="abs doc-title" style="left:232px;top:2484px">Purchase Agreement</div>
<div class="abs doc-sub" style="left:232px;top:2516px">Uploaded by Chloe Buyer</div>
<div class="abs btn-outline" style="left:462px;top:2485px;width:99px;height:50px">VIEW</div>

<div class="abs btn-fill" style="left:280px;top:2560px;width:166px;height:49px">DOWNLOAD ALL</div>

<!-- wiring panel -->
<div class="abs panel" style="left:606px;top:2171px;width:459px;height:470px">
  <div class="panel-title">WIRING INSTRUCTIONS</div>
  <div class="panel-rule"></div>
</div>
<div class="abs" style="left:640px;top:2265px">
  <div class="wire-label">Bank Name</div><div class="wire-value" style="margin-bottom:12px">ABC International Bank</div>
  <div class="wire-label">Bank Address</div><div class="wire-value" style="margin-bottom:12px">mi ipsum faucibus vitae aliquet</div>
  <div class="wire-label">Bank Phone</div><div class="wire-value" style="margin-bottom:12px">972532646</div>
  <div class="wire-label">Bank ABA Number</div><div class="wire-value" style="margin-bottom:12px">ABA 1281465</div>
  <div class="wire-label">Acoount Number</div><div class="wire-value" style="margin-bottom:12px">0004725 94835200002</div>
  <div class="wire-label">Any Additional Information</div><div class="wire-value">Everything Clear</div>
</div>
<div class="abs btn-fill" style="left:711px;top:2560px;width:249px;height:49px">DOWNLOAD DOCUMENT</div>

<!-- professionals -->
<div class="abs rule" style="left:136px;top:2745px;width:170px"></div>
<div class="abs dot" style="left:295px;top:2740px"></div>
<div class="abs dot" style="left:888px;top:2740px"></div>
<div class="abs rule" style="left:894px;top:2745px;width:171px"></div>
<div class="abs section-head" style="top:2726px">YOUR REAL ESTATE PROFESSIONALS</div>

<div class="abs photo" style="left:135px;top:2828px;background:linear-gradient(160deg,#3a3430,#7a6a60 60%,#c7b8ad)" role="img" aria-label="Portrait photo of Emily Johnson"></div>
<div class="abs pro-name" style="left:135px;top:3055px">Emily Johnson</div>
<div class="abs pro-co" style="left:135px;top:3088px">The Real Estate Law Firm</div>
<div class="abs btn-outline" style="left:135px;top:3125px;width:82px;height:40px">VIEW</div>

<div class="abs photo" style="left:494px;top:2828px;background:linear-gradient(160deg,#9aa0a4,#5a5f63 55%,#1f2227)" role="img" aria-label="Portrait photo of Bob Buyer Agent"></div>
<div class="abs pro-name" style="left:494px;top:3055px">Bob Buyer Agent</div>
<div class="abs pro-co" style="left:494px;top:3088px">Bob Real Estate</div>
<div class="abs btn-outline" style="left:494px;top:3125px;width:82px;height:40px">VIEW</div>

<div class="abs photo" style="left:856px;top:2828px;background:linear-gradient(160deg,#111,#555 55%,#8a8a8a)" role="img" aria-label="Portrait photo of Larry Loan Officer"></div>
<div class="abs pro-name" style="left:856px;top:3055px">Larry Loan Officer</div>
<div class="abs pro-co" style="left:856px;top:3088px">Larry Mortgages</div>
<div class="abs btn-outline" style="left:856px;top:3125px;width:82px;height:40px">VIEW</div>

<!-- contact icon buttons -->
<div class="abs icon-btn" style="left:245px;top:3125px"><svg width="20" height="14" viewBox="0 0 20 14"><rect x="1" y="1" width="18" height="12" fill="none" stroke="#fff" stroke-width="1.8"/><path d="M1 1l9 7 9-7" fill="none" stroke="#fff" stroke-width="1.8"/></svg></div>
<div class="abs icon-btn" style="left:301px;top:3125px"><svg width="18" height="18" viewBox="0 0 24 24"><path d="M6.6 10.8a15 15 0 0 0 6.6 6.6l2.2-2.2a1 1 0 0 1 1-.25 11.4 11.4 0 0 0 3.6.57 1 1 0 0 1 1 1V20a1 1 0 0 1-1 1A17 17 0 0 1 3 4a1 1 0 0 1 1-1h3.5a1 1 0 0 1 1 1c0 1.25.2 2.45.57 3.57a1 1 0 0 1-.25 1z" fill="#fff"/></svg></div>
<div class="abs icon-btn" style="left:604px;top:3125px"><svg width="20" height="14" viewBox="0 0 20 14"><rect x="1" y="1" width="18" height="12" fill="none" stroke="#fff" stroke-width="1.8"/><path d="M1 1l9 7 9-7" fill="none" stroke="#fff" stroke-width="1.8"/></svg></div>
<div class="abs icon-btn" style="left:660px;top:3125px"><svg width="18" height="18" viewBox="0 0 24 24"><path d="M6.6 10.8a15 15 0 0 0 6.6 6.6l2.2-2.2a1 1 0 0 1 1-.25 11.4 11.4 0 0 0 3.6.57 1 1 0 0 1 1 1V20a1 1 0 0 1-1 1A17 17 0 0 1 3 4a1 1 0 0 1 1-1h3.5a1 1 0 0 1 1 1c0 1.25.2 2.45.57 3.57a1 1 0 0 1-.25 1z" fill="#fff"/></svg></div>
<div class="abs icon-btn" style="left:966px;top:3125px"><svg width="20" height="14" viewBox="0 0 20 14"><rect x="1" y="1" width="18" height="12" fill="none" stroke="#fff" stroke-width="1.8"/><path d="M1 1l9 7 9-7" fill="none" stroke="#fff" stroke-width="1.8"/></svg></div>
<div class="abs icon-btn" style="left:1022px;top:3125px"><svg width="18" height="18" viewBox="0 0 24 24"><path d="M6.6 10.8a15 15 0 0 0 6.6 6.6l2.2-2.2a1 1 0 0 1 1-.25 11.4 11.4 0 0 0 3.6.57 1 1 0 0 1 1 1V20a1 1 0 0 1-1 1A17 17 0 0 1 3 4a1 1 0 0 1 1-1h3.5a1 1 0 0 1 1 1c0 1.25.2 2.45.57 3.57a1 1 0 0 1-.25 1z" fill="#fff"/></svg></div>

<!-- faq -->
<div class="abs rule" style="left:136px;top:3245px;width:194px"></div>
<div class="abs dot" style="left:324px;top:3240px"></div>
<div class="abs dot" style="left:858px;top:3240px"></div>
<div class="abs rule" style="left:864px;top:3245px;width:201px"></div>
<div class="abs section-head" style="top:3226px">FREQUENTLY ASKED QUESTIONS</div>

<div class="abs faq" style="left:135px;top:3301px;width:928px;height:109px">
  <div class="faq-q" style="top:18px">What Should I expect at closing?</div>
  <div class="faq-a">Lorem ipsum dolor sit amet, consectetur adipiscing elit, sed do eiusmod tempor incididunt ut labore et dolore magna aliqua. Vel elit scelerisque mauris pellentesque.</div>
  <svg class="faq-chev" style="top:48px" width="16" height="10" viewBox="0 0 16 10"><path d="M2 8l6-6 6 6" fill="none" stroke="#fff" stroke-width="2"/></svg>
</div>
<div class="abs faq" style="left:133px;top:3425px;width:930px;height:66px">
  <div class="faq-q" style="top:21px">What is Title Insurance?</div>
  <svg class="faq-chev" style="top:28px" width="16" height="10" viewBox="0 0 16 10"><path d="M2 2l6 6 6-6" fill="none" stroke="#fff" stroke-width="2"/></svg>
</div>
<div class="abs faq" style="left:131px;top:3506px;width:933px;height:65px">
  <div class="faq-q" style="left:24px;top:21px">What is Title Insurance?</div>
  <svg class="faq-chev" style="top:28px" width="16" height="10" viewBox="0 0 16 10"><path d="M2 2l6 6 6-6" fill="none" stroke="#fff" stroke-width="2"/></svg>
</div>

<!-- footer -->
<svg class="abs footer" viewBox="0 0 1200 285" preserveAspectRatio="none"><polygon points="0,46 600,0 1200,46 1200,285 0,285" fill="#2ea3d8"/></svg>
<div class="abs footer-text" style="left:267px;top:3692px">
  <svg width="14" height="14" viewBox="0 0 24 24"><path d="M6.6 10.8a15 15 0 0 0 6.6 6.6l2.2-2.2a1 1 0 0 1 1-.25 11.4 11.4 0 0 0 3.6.57 1 1 0 0 1 1 1V20a1 1 0 0 1-1 1A17 17 0 0 1 3 4a1 1 0 0 1 1-1h3.5a1 1 0 0 1 1 1c0 1.25.2 2.45.57 3.57a1 1 0 0 1-.25 1z" fill="#fff"/></svg>(305) 555-0142
</div>
<div class="abs footer-logo">Veltrana</div>
<div class="abs footer-text" style="left:802px;top:3692px">
  <svg width="18" height="13" viewBox="0 0 20 14"><rect x="1" y="1" width="18" height="12" fill="none" stroke="#fff" stroke-width="1.8"/><path d="M1 1l9 7 9-7" fill="none" stroke="#fff" stroke-width="1.8"/></svg>mail@veltrana.com
</div>
<div class="abs footer-text" style="left:0;top:3779px;width:1200px;justify-content:center;gap:6px">
  <svg width="10" height="14" viewBox="0 0 24 32"><path d="M12 1a10 10 0 0 1 10 10c0 8-10 20-10 20S2 19 2 11A10 10 0 0 1 12 1z" fill="#fff"/><circle cx="12" cy="11" r="4" fill="#2ea3d8"/></svg>1820 Harbor Lane, Suite 210 Miami, Florida 33155
</div>
<div class="abs footer-copy">©&nbsp; 2021 Veltrana™. All Rights Reserved | Privacy Policy | Terms and Use</div>

</body>
</html>
```